Video Production Company Website

A video production company website for "Amber Brook Productions"
Home page must have video player and way to select between 3 different videos.

Company does video Post production : Editing, Motion Graphics, Color correction, and Aerial videography
Attached company Logo

Design should be simple but Pro looking..

Earthy color palette with slight texture..

Industry/Entity Type

Film Production

Number of Pages Required

3 page

Font styles to use
Sans Serif
Other font styles liked:
• Font Attached

Requirements
Nice to have
• Thumbnails on homepage to past project clips
Should not have
• full page video

```html
<!DOCTYPE html>
<html lang="en">
<head>
<meta charset="utf-8">
<title>Amber Brook Productions</title>
<link href="https://fonts.googleapis.com/css2?family=Poppins:wght@300;400;500;600;700&display=swap" rel="stylesheet">
<style>
:root{
  --teal:#1f9c90;
  --ink:#2b2b2b;
  --heading:#5a5a5a;
  --muted:#9a9a9a;
  --line:#dcdcdc;
  --white:#ffffff;
  --night-top:#1a2340;
  --night-mid:#3a3f6e;
  --night-glow:#b86a6a;
  --night-ground:#14161c;
}
*{margin:0;padding:0;box-sizing:border-box}
html,body{width:1200px;height:2816px;overflow:hidden;background:var(--white);font-family:'Poppins',sans-serif;color:var(--ink)}
.page{position:relative;width:1200px;height:2816px}

.site-header{position:absolute;top:0;left:0;width:1200px;height:72px;display:flex;align-items:center;justify-content:space-between;padding:0 24px 0 22px}
.brand{display:flex;align-items:center;gap:10px;font-size:19px;font-weight:700;color:var(--ink);letter-spacing:.2px}
.brand-dot{width:12px;height:12px;border-radius:50%;background:var(--ink)}
.menu-toggle{display:flex;align-items:center;gap:8px;font-size:15px;font-weight:500;letter-spacing:1px;color:var(--ink)}

.hero{position:absolute;top:72px;left:0;width:1200px;height:543px;overflow:hidden;
  background:radial-gradient(ellipse at 55% 75%,var(--night-glow) 0%,rgba(184,106,106,0) 40%),
             linear-gradient(180deg,var(--night-top) 0%,var(--night-mid) 55%,#57485e 68%,var(--night-ground) 82%)}
.hero-title{position:absolute;top:104px;left:0;width:100%;text-align:center;color:var(--white);font-size:54px;font-weight:500;letter-spacing:2px}
.hero-sub{position:absolute;top:190px;left:0;width:100%;text-align:center;color:var(--white);font-size:17px;font-weight:500;letter-spacing:4px}
.play-btn{position:absolute;top:266px;left:572px;width:56px;height:56px}
.video-thumbs{position:absolute;top:414px;left:260px;display:flex;gap:24px}
.thumb{width:208px;height:104px}
.thumb.active{outline:3px solid rgba(255,255,255,.85);outline-offset:-3px}
.thumb-stars{background:linear-gradient(160deg,#1d2a55,#3d4a7a 60%,#6a5a4a)}
.thumb-field{background:linear-gradient(180deg,#0d1a0f,#2b3f1c 60%,#6e6a2a)}
.thumb-fruit{background:radial-gradient(circle at 40% 60%,#d86a22 0%,#8a3a14 30%,#1a120e 70%)}

.intro{position:absolute;top:690px;left:0;width:1200px;text-align:center}
.section-title{font-size:35px;font-weight:400;color:var(--heading);letter-spacing:2px}
.intro-text{width:760px;margin:34px auto 0;font-size:13px;line-height:22px;color:var(--muted)}
.outline-btn{display:inline-block;width:180px;height:46px;line-height:44px;border:1px solid var(--teal);color:var(--teal);font-size:12px;font-weight:500;letter-spacing:2px;text-align:center}
.intro .outline-btn{margin-top:48px}

.projects-label{position:absolute;top:1008px;left:0;width:1200px;text-align:center;font-size:15px;font-weight:500;letter-spacing:2px;color:var(--heading)}
.project-grid{position:absolute;top:1068px;left:0;width:1200px;display:grid;grid-template-columns:600px 600px;grid-template-rows:400px 392px}
.tile{position:relative}
.tile-dinner{background:linear-gradient(135deg,#5a4432,#a48462 45%,#3b2c22)}
.tile-guitar{background:radial-gradient(ellipse at 50% 30%,#6d7178 0%,#2c2f34 55%,#121315)}
.tile-honey{background:radial-gradient(ellipse at 40% 60%,#c98a1e 0%,#7a4a14 35%,#1c1e22 70%)}
.tile-food{background:linear-gradient(160deg,#3a3f42,#4e5356 50%,#2a2d2f)}
.tile-overlay{position:absolute;inset:0;background:rgba(20,22,24,.45);display:flex;flex-direction:column;align-items:center;justify-content:center;color:var(--white)}
.tile-name{font-size:30px;font-weight:400;letter-spacing:3px}
.tile-rule{width:180px;height:1px;background:rgba(255,255,255,.7);margin:10px 0 12px}
.tile-type{font-size:13px;letter-spacing:.5px}
.tile-eye{margin-top:16px}

.contact{position:absolute;top:1932px;left:0;width:1200px;text-align:center}
.contact-note{margin-top:34px;font-size:12px;color:var(--muted)}
.contact-form{position:relative;width:600px;margin:34px auto 0;text-align:left}
.field-row{display:flex;gap:26px}
.field{flex:1;height:58px;border-bottom:1px solid var(--line);padding-top:18px;font-size:11px;color:#777}
.field-wide{height:90px}
.contact .outline-btn{margin-top:46px}

.site-footer{position:absolute;top:2456px;left:0;width:1200px;border-top:1px solid #ececec;text-align:center}
.footer-nav{margin-top:88px;display:flex;justify-content:center;gap:46px;font-size:12px;font-weight:500;letter-spacing:1.5px;color:var(--teal)}
.footer-info{margin-top:56px;font-size:11px;line-height:22px;color:var(--muted)}
.social{margin-top:34px;display:flex;justify-content:center;gap:22px}
.social-dot{width:22px;height:22px;border-radius:50%;background:var(--teal)}
</style>
</head>
<body>
<div class="page">

  <header class="site-header">
    <div class="brand"><span class="brand-dot"></span>Amber Brook Productions</div>
    <div class="menu-toggle">MENU
      <svg width="18" height="14" viewBox="0 0 18 14"><rect y="0" width="18" height="2.4" fill="#2b2b2b"/><rect y="5.8" width="18" height="2.4" fill="#2b2b2b"/><rect y="11.6" width="18" height="2.4" fill="#2b2b2b"/></svg>
    </div>
  </header>

  <section class="hero" role="img" aria-label="Night landscape with starry sky and silhouetted trees, video player">
    <h1 class="hero-title">THE BEST OF THE NIGHTS</h1>
    <p class="hero-sub">COLOR CORRECTION</p>
    <svg class="play-btn" viewBox="0 0 56 56"><circle cx="28" cy="28" r="28" fill="#ffffff"/><path d="M22 17 L39 28 L22 39 Z" fill="#1d1d1d"/></svg>
    <div class="video-thumbs">
      <div class="thumb thumb-stars active" role="img" aria-label="Video thumbnail: starry night sky"></div>
      <div class="thumb thumb-field" role="img" aria-label="Video thumbnail: fireflies over a field"></div>
      <div class="thumb thumb-fruit" role="img" aria-label="Video thumbnail: fresh fruit close-up"></div>
    </div>
  </section>

  <section class="intro">
    <h2 class="section-title">WE CREATE MASTERPIECE</h2>
    <p class="intro-text">Sed ut perspiciatis unde omnis iste natus error sit voluptatem accusantium doloremque laudantium, totam rem aperiam, eaque ipsa quae ab illo inventore veritatis et quasi architecto beatae vitae dicta.</p>
    <a class="outline-btn">SEE OUR WORKS</a>
  </section>

  <h3 class="projects-label">OUR LATEST PROJECTS</h3>
  <section class="project-grid">
    <div class="tile tile-dinner" role="img" aria-label="Project: family sharing dinner at a restaurant"></div>
    <div class="tile tile-guitar" role="img" aria-label="Project: guitarist standing in an industrial hall"></div>
    <div class="tile tile-honey" role="img" aria-label="Project: honeycomb with a wooden honey dipper"></div>
    <div class="tile tile-food" role="img" aria-label="Project: food ingredients on a slate board">
      <div class="tile-overlay">
        <div class="tile-name">FOOD WORLD</div>
        <div class="tile-rule"></div>
        <div class="tile-type">Motion Graphics</div>
        <svg class="tile-eye" width="22" height="14" viewBox="0 0 22 14"><path d="M1 7 Q11 -3 21 7 Q11 17 1 7 Z" fill="none" stroke="#ffffff" stroke-width="1.6"/><circle cx="11" cy="7" r="3" fill="#ffffff"/></svg>
      </div>
    </div>
  </section>

  <section class="contact">
    <h2 class="section-title">START PROJECT NOW</h2>
    <p class="contact-note">Fill out the form below or send us an email hello@amberbrookproductions.com and we will contact you shortly.</p>
    <div class="contact-form">
      <div class="field-row"><div class="field">Your Name &amp; Company *</div><div class="field">Your Email Address</div></div>
      <div class="field-row"><div class="field">Your Phone Number *</div><div class="field">Website URL</div></div>
      <div class="field-row"><div class="field field-wide">Your Message</div></div>
    </div>
    <a class="outline-btn">SEND MESSAGE</a>
  </section>

  <footer class="site-footer">
    <nav class="footer-nav"><span>HOME</span><span>OUR WORK</span><span>SERVICES</span><span>THE COMPANY</span><span>BLOG</span><span>CONTACT</span></nav>
    <p class="footer-info">© 418 Cedar Lane Fairview CA 90000 &nbsp;|&nbsp; Amber Brook Productions &nbsp;|&nbsp; All Rights Reserved<br>555-0142 &nbsp;|&nbsp; Call us any time</p>
    <div class="social"><span class="social-dot"></span><span class="social-dot"></span><span class="social-dot"></span><span class="social-dot"></span></div>
  </footer>

</div>
</body>
</html>
```